Website re-design

We are a successful furnished apartment provider in Boston. We currently are working on re-designing our website www.ribtenlofts.com to make it more modern, designer look and user friendly. We hired a designer, but are not happy with the designs proposed and want to improve on them. The winning design will be paid regardless of whether we stay with our current designer or not. We want ideas and functional page links to see how it will work. Platform we have chosen is wordpress. Feel free to propose others easy for us to update and modify. We do not like Joomla on which website is currently running. We do not like flash nor long load times.
Please use photos on our website for design presentations. www.ribtenlofts.com

Target Market(s)

doctors, nurses, business men but mostly business women, some post-medical students

Industry/Entity Type

Apartment

Requirements
Must have
• Quick action button for reservation form and a notification and email forwarding system to us of reservation information by potential clients. Blog required with feedback by guests allowed, we can censor which are published. Slide shows of apartments.
Should not have
• No movies.

```html
<!DOCTYPE html>
<html lang="en">
<head>
<meta charset="utf-8">
<title>Ribten Lofts – Furnished Apartment</title>
<link href="https://fonts.googleapis.com/css2?family=PT+Sans:wght@400;700&family=Arimo:ital,wght@0,400;0,700;1,400&display=swap" rel="stylesheet">
<style>
:root{
  --page:#ffffff;
  --ink:#1f1f1f;
  --body-text:#555555;
  --gold:#c2a45a;
  --gold-dark:#a8893c;
  --link-blue:#2f86c4;
  --badge-green:#8cc63f;
  --badge-blue:#3a8fc4;
  --wall-light:#f3efe6;
  --wall-mid:#e3dccb;
  --strip:#ececec;
  --footer:#232323;
  --footer-base:#1a1a1a;
  --footer-rule:#3a3a3a;
  --footer-text:#d8d8d8;
}
*{box-sizing:border-box;margin:0;padding:0}
html,body{width:1158px;height:1200px;overflow:hidden;background:var(--page)}
body{position:relative;font-family:"Arimo",Arial,sans-serif;color:var(--ink)}
.abs{position:absolute}

/* header */
.site-header{left:0;top:0;width:1158px;height:84px}
.header-shape{position:absolute;left:0;top:0}
.brand{left:189px;top:13px;display:flex;align-items:center;gap:10px}
.brand-mark{width:58px;height:58px;border-radius:50%;background:var(--gold)}
.brand-name{font-family:"PT Sans",sans-serif;font-weight:400;font-size:29px;line-height:30px;color:#2b2b2b;letter-spacing:.5px}
.brand-tag{font-family:"PT Sans",sans-serif;font-size:13px;color:#2b2b2b;letter-spacing:.6px;margin-top:2px}
.main-nav{left:513px;top:24px;display:flex;font-family:"PT Sans",sans-serif;font-size:12.3px;color:#333}
.main-nav a{color:#333;text-decoration:none;padding:0 6px;border-left:1px solid #333;line-height:12px}
.main-nav a:first-child{border-left:0;padding-left:0;color:var(--gold-dark)}
.main-nav a:last-child{padding-right:0}

/* hero */
.hero-band{left:0;top:84px;width:1158px;height:351px;background:linear-gradient(90deg,var(--wall-mid),var(--wall-light) 30%,var(--wall-light) 70%,var(--wall-mid))}
.hero-slide{left:189px;top:108px;width:781px;height:350px;border-radius:0 0 14px 14px;overflow:hidden;
  background:linear-gradient(160deg,#b8a98a 0%,#8a7152 30%,#4e3a28 55%,#3a2f4a 75%,#6d5a3e 100%)}
.hero-shadow{left:189px;top:458px;width:781px;height:24px;background:linear-gradient(#d9d9d9,rgba(255,255,255,0));border-radius:0 0 40px 40px}
.caption-band{position:absolute;left:0;top:0}
.caption-title{left:15px;top:282px;font-family:"PT Sans",sans-serif;font-weight:700;font-size:15px;color:#fff;letter-spacing:.3px}
.caption-text{left:15px;top:301px;width:345px;font-weight:700;font-size:11px;line-height:13.5px;color:#fff}
.quick-link{top:310px;display:flex;align-items:center;gap:8px;font-family:"PT Sans",sans-serif;font-weight:700;font-size:11.5px;line-height:14px;color:#fff;letter-spacing:.3px}
.quick-link svg{flex:none;display:block}
.slide-arrow{top:268px;width:32px;height:32px;border-radius:50%;background:#1e1e1e;border:2px solid #4a4a4a}
.slide-arrow svg{position:absolute;left:9px;top:9px}

/* welcome */
.welcome-title{left:189px;top:508px;font-family:"PT Sans",sans-serif;font-weight:700;font-size:19px;color:#111}
.welcome-title strong{font-size:26px}
.welcome-copy{left:189px;top:544px;width:492px;font-size:12px;line-height:15.2px;color:var(--body-text)}
.welcome-copy p+p{margin-top:15px}

/* news */
.news{left:754px;top:514px;width:212px}
.news h2{font-family:"PT Sans",sans-serif;font-weight:400;font-size:19px;color:#111}
.news-sub{font-style:italic;font-size:9.5px;color:#777;margin-top:2px}
.news-item{position:relative;height:96px;margin-top:12px}
.news-item+.news-item{border-top:1px solid #cfcfcf;margin-top:0}
.date-badge{position:absolute;left:3px;top:6px;width:36px;height:40px;border-radius:4px;background:#f2f2f2;box-shadow:0 2px 3px rgba(0,0,0,.25);overflow:hidden;text-align:center}
.date-badge .m{display:block;background:var(--badge-green);color:#fff;font-size:8.5px;font-weight:700;line-height:12px}
.date-badge .d{display:block;color:var(--badge-blue);font-size:17px;font-weight:700;line-height:26px}
.news-item h3{position:absolute;left:49px;top:8px;font-size:10.5px;font-weight:700;color:#111}
.news-item p{position:absolute;left:49px;top:25px;width:150px;font-size:9.5px;line-height:14.5px;color:#444}
.news-item .more{position:absolute;right:14px;top:73px;font-size:9.5px;font-weight:700;color:var(--link-blue)}
.news-item + .news-item .date-badge{top:20px}
.news-item + .news-item h3{top:21px}
.news-item + .news-item p{top:38px}
.news-item + .news-item .more{top:86px}

/* gallery strip */
.gallery{left:0;top:759px;width:1158px;height:129px;background:var(--strip);border-top:1px solid #d6d6d6;border-bottom:1px solid #d6d6d6}
.thumb{top:9px;width:144px;height:108px;background:#fff;padding:5px;box-shadow:0 1px 3px rgba(0,0,0,.3)}
.thumb div{width:100%;height:100%}
.thumb-a{background:linear-gradient(170deg,#dfe6ea,#f5f5f2 45%,#6f8a4e 80%,#3f5a2e)}
.thumb-b{background:linear-gradient(170deg,#7aa4d8,#b4694e 50%,#4f6b3a 85%)}
.thumb-c{background:linear-gradient(170deg,#e7ecef,#c9d4cf 50%,#7f9870 85%)}
.thumb-shadow{top:117px;width:144px;height:10px;background:radial-gradient(ellipse at top,rgba(0,0,0,.28),rgba(0,0,0,0) 70%)}
.gallery-arrow{top:49px}

/* footer */
.footer-rule{left:0;top:888px;width:1158px;height:6px;background:#3b3b3b}
.site-footer{left:0;top:894px;width:1158px;height:260px;background:var(--footer)}
.footer-col{top:32px;width:240px}
.footer-col h2{font-family:"PT Sans",sans-serif;font-weight:700;font-size:15px;color:#fff;letter-spacing:.2px}
.post{position:relative;height:64px}
.post:first-of-type{margin-top:14px}
.post:nth-of-type(3){height:60px}
.post-thumb{position:absolute;left:0;top:0;width:46px;height:54px;border:2px solid #ececec;background:linear-gradient(135deg,#f2c21b,#d99a12 55%,#6b5a3a)}
.post h3{position:absolute;left:59px;top:2px;font-size:10.5px;font-weight:700;color:#fff}
.post p{position:absolute;left:59px;top:14px;width:180px;font-size:10.5px;line-height:12px;color:var(--footer-text)}
.post .more{position:absolute;left:59px;top:40px;font-size:10.5px;font-weight:700;color:#fff}
.footer-divider{top:52px;width:1px;height:186px;background:var(--footer-rule)}
.footer-base{left:0;top:1154px;width:1158px;height:46px;background:var(--footer-base);border-top:1px solid #333}
.footer-brand{left:189px;top:8px;display:flex;align-items:center;gap:10px}
.footer-mark{width:30px;height:30px;border-radius:50%;background:#9a9a9a}
.footer-name{font-family:"PT Sans",sans-serif;font-size:21px;line-height:20px;color:#e6e6e6;letter-spacing:.5px}
.footer-tag{font-family:"PT Sans",sans-serif;font-size:9.5px;color:#bdbdbd;letter-spacing:.6px}
.social{left:823px;top:14px;display:flex;gap:2px}
.social span{width:19px;height:19px;border-radius:3px;display:block}
</style>
</head>
<body>

<header class="abs site-header">
  <svg class="header-shape" width="1158" height="84" viewBox="0 0 1158 84" aria-hidden="true">
    <defs>
      <linearGradient id="headerFade" x1="0" y1="0" x2="0" y2="1">
        <stop offset="0" stop-color="#f4f4f4"/>
        <stop offset="1" stop-color="#e2e2e2"/>
      </linearGradient>
    </defs>
    <rect width="1158" height="84" fill="url(#headerFade)"/>
    <path d="M0 84 L430 84 C452 84 455 58 480 58 L1158 58 L1158 84 Z" fill="#ffffff"/>
  </svg>
  <div class="abs brand">
    <span class="brand-mark"></span>
    <div>
      <div class="brand-name">RIBTEN LOFTS</div>
      <div class="brand-tag">FURNISHED APARTMENT</div>
    </div>
  </div>
  <nav class="abs main-nav">
    <a href="#">Home</a><a href="#">About Us</a><a href="#">Apartments</a><a href="#">Boston</a><a href="#">Reservations</a><a href="#">Blog</a><a href="#">Reviews</a><a href="#">Contact Us</a>
  </nav>
</header>

<section class="abs hero-band"></section>
<div class="abs hero-shadow"></div>
<section class="abs hero-slide" role="img" aria-label="Slideshow photo of a furnished apartment bedroom with armchairs, bed and windows">
  <svg class="caption-band" width="781" height="350" viewBox="0 0 781 350" aria-hidden="true">
    <path d="M0 274 Q0 274 6 272 L330 272 C346 272 348 300 368 300 L781 300 L781 350 L0 350 Z" fill="rgba(10,10,10,.82)"/>
  </svg>
  <div class="abs caption-title">HIGH PRICE APPARTMENT</div>
  <div class="abs caption-text">Lorem Ipsum is simply dummy text of the printing and typesetting industry. Lorem Ipsum has been the industry's standard dummy text ever since the 1500s.</div>
  <div class="abs quick-link" style="left:538px">
    <svg width="20" height="18" viewBox="0 0 20 18" aria-hidden="true"><path d="M2 8 Q10 0 18 8 Q14 6 10 7 Q6 6 2 8 Z" fill="#fff"/><path d="M10 7 L13 17" stroke="#fff" stroke-width="1.6"/></svg>
    <span>APPARTMENT<br>RESERVATION</span>
  </div>
  <div class="abs quick-link" style="left:661px">
    <svg width="28" height="28" viewBox="0 0 28 28" aria-hidden="true"><circle cx="12" cy="12" r="9" fill="none" stroke="#fff" stroke-width="3"/><path d="M18.5 18.5 L25 25" stroke="#fff" stroke-width="4" stroke-linecap="round"/></svg>
    <span>APPARTMENT<br>DESCRIPTION</span>
  </div>
</section>
<a class="abs slide-arrow" href="#" style="left:173px" aria-label="Previous slide"><svg width="12" height="12" viewBox="0 0 12 12"><path d="M8 1 L3 6 L8 11" fill="none" stroke="#fff" stroke-width="2.4"/></svg></a>
<a class="abs slide-arrow" href="#" style="left:954px" aria-label="Next slide"><svg width="12" height="12" viewBox="0 0 12 12"><path d="M4 1 L9 6 L4 11" fill="none" stroke="#fff" stroke-width="2.4"/></svg></a>

<h1 class="abs welcome-title">WELLCOME TO <strong>RIBTEN LOFTS</strong></h1>
<div class="abs welcome-copy">
  <p>Lorem Ipsum is simply dummy text of the printing and typesetting industry. Lorem Ipsum has been the industry's standard dummy text ever since the 1500s, when an unknown printer took a galley of type and scrambled it to make a type specimen book. It has survived not only five centuries, but also the leap into electronic typesetting, remaining essentially unchanged. It was popularised in the 1960s with the release of Lettrafold sheets containing Lorem Ipsum passages, and more recently with desktop publishing software like Folio LayoutDesk including versions of Lorem Ipsum.</p>
  <p>It is a long established fact that a reader will be distracted by the readable content of a page when looking at its layout. The point of using Lorem Ipsum is that it has a more-or-less normal distribution of letters, as opposed to using 'Content here, content here', making it look like readable English.</p>
</div>

<aside class="abs news">
  <h2>Latest News/Events:</h2>
  <div class="news-sub">Lorem ipsum dolor sit amet, consectetur.</div>
  <article class="news-item">
    <div class="date-badge"><span class="m">NOV</span><span class="d">05</span></div>
    <h3>Lorem Ipsum dolor sit amet</h3>
    <p>Lorem Ipsum is simply dummy text of the printing and typesetting industry.</p>
    <a class="more">Read More</a>
  </article>
  <article class="news-item">
    <div class="date-badge"><span class="m">NOV</span><span class="d">05</span></div>
    <h3>Lorem Ipsum dolor sit amet</h3>
    <p>Lorem Ipsum is simply dummy text of the printing and typesetting industry.</p>
    <a class="more">Read More</a>
  </article>
</aside>

<section class="abs gallery">
  <svg class="abs gallery-arrow" style="left:176px" width="14" height="32" viewBox="0 0 14 32" aria-label="Previous"><path d="M12 1 L2 16 L12 31" fill="none" stroke="#999" stroke-width="2"/></svg>
  <div class="abs thumb" style="left:196px"><div class="thumb-a" role="img" aria-label="Photo of a modern white apartment building"></div></div>
  <div class="abs thumb" style="left:353px"><div class="thumb-b" role="img" aria-label="Photo of a red and grey apartment building"></div></div>
  <div class="abs thumb" style="left:510px"><div class="thumb-c" role="img" aria-label="Photo of a pale apartment building with palm trees"></div></div>
  <div class="abs thumb" style="left:667px"><div class="thumb-a" role="img" aria-label="Photo of a modern white apartment building"></div></div>
  <div class="abs thumb" style="left:824px"><div class="thumb-b" role="img" aria-label="Photo of a red and grey apartment building"></div></div>
  <div class="abs thumb-shadow" style="left:196px"></div>
  <div class="abs thumb-shadow" style="left:353px"></div>
  <div class="abs thumb-shadow" style="left:510px"></div>
  <div class="abs thumb-shadow" style="left:667px"></div>
  <div class="abs thumb-shadow" style="left:824px"></div>
  <svg class="abs gallery-arrow" style="left:970px" width="14" height="32" viewBox="0 0 14 32" aria-label="Next"><path d="M2 1 L12 16 L2 31" fill="none" stroke="#999" stroke-width="2"/></svg>
</section>

<div class="abs footer-rule"></div>
<footer class="abs site-footer">
  <div class="abs footer-col" style="left:189px">
    <h2>LATEST BLOG POSTS:</h2>
    <div class="post"><div class="post-thumb" role="img" aria-label="Blog post photo"></div><h3>Heading 1</h3><p>Lorem Ipsum is simply dummy text of the printing and typesetting industry.</p><a class="more">+ Read More</a></div>
    <div class="post"><div class="post-thumb" role="img" aria-label="Blog post photo"></div><h3>Heading 2</h3><p>Lorem Ipsum is simply dummy text of the printing and typesetting industry.</p><a class="more">+ Read More</a></div>
    <div class="post"><div class="post-thumb" role="img" aria-label="Blog post photo"></div><h3>Heading 3</h3><p>Lorem Ipsum is simply dummy text of the printing and typesetting industry.</p><a class="more">+ Read More</a></div>
  </div>
  <div class="abs footer-divider" style="left:441px"></div>
  <div class="abs footer-col" style="left:468px">
    <h2>FRIENDBOOK UPDATES:</h2>
    <div class="post"><div class="post-thumb" role="img" aria-label="Update photo"></div><h3>Heading 1</h3><p>Lorem Ipsum is simply dummy text of the printing and typesetting industry.</p><a class="more">+ Read More</a></div>
    <div class="post"><div class="post-thumb" role="img" aria-label="Update photo"></div><h3>Heading 2</h3><p>Lorem Ipsum is simply dummy text of the printing and typesetting industry.</p><a class="more">+ Read More</a></div>
    <div class="post"><div class="post-thumb" role="img" aria-label="Update photo"></div><h3>Heading 3</h3><p>Lorem Ipsum is simply dummy text of the printing and typesetting industry.</p><a class="more">+ Read More</a></div>
  </div>
  <div class="abs footer-divider" style="left:718px"></div>
  <div class="abs footer-col" style="left:742px">
    <h2>CHIRPER POSTS:</h2>
    <div class="post"><div class="post-thumb" role="img" aria-label="Post photo"></div><h3>Heading 1</h3><p>Lorem Ipsum is simply dummy text of the printing and typesetting industry.</p><a class="more">+ Read More</a></div>
    <div class="post"><div class="post-thumb" role="img" aria-label="Post photo"></div><h3>Heading 2</h3><p>Lorem Ipsum is simply dummy text of the printing and typesetting industry.</p><a class="more">+ Read More</a></div>
    <div class="post"><div class="post-thumb" role="img" aria-label="Post photo"></div><h3>Heading 3</h3><p>Lorem Ipsum is simply dummy text of the printing and typesetting industry.</p><a class="more">+ Read More</a></div>
  </div>
</footer>

<div class="abs footer-base">
  <div class="abs footer-brand">
    <span class="footer-mark"></span>
    <div>
      <div class="footer-name">RIBTEN LOFTS</div>
      <div class="footer-tag">FURNISHED APARTMENT ©2012</div>
    </div>
  </div>
  <div class="abs social" aria-label="Social links">
    <span style="background:#4aa3d8"></span>
    <span style="background:#3b5a98"></span>
    <span style="background:#2a77b0"></span>
    <span style="background:#e8892b"></span>
    <span style="background:#555a66"></span>
    <span style="background:#5a6e9c"></span>
    <span style="background:#c8332b"></span>
    <span style="background:#3aa8c9"></span>
  </div>
</div>

</body>
</html>
```